Frame And Form Biz Card Design

That example is too complicated. Frame And Form is my home design business.

I design Interiors, Exteriors and Home Staging.

My tag line is: BRINGING BRIGHT IDEAS TO INTERIORS, EXTERIORS AND HOME STAGING.

I would like a clean, simple, modern (sort of Helvetica-ish) design that includes an image of a light bulb. The bulb and the text should blend seamlessly.

I prefer a white background; black text; and blue highlights (lightbulb); not a greenish blue, not a navy blue. A color that mixes the best of both. Green/Blue. Not turquoise.

The color scheme should be elegant. And modern. Professional. Not quite 'too hip for the room'.

Sorta ignore the logo design example that is attached.

Let me know any questions! Look forward, thank you Megan

Megan T Dulcoff
Senior Design Specialist
Tel: 240-555-0193
Web: megan@frameandform.example

```html
<!DOCTYPE html>
<html lang="en">
<head>
<meta charset="utf-8">
<title>Frame And Form – Business Card</title>
<link rel="stylesheet" href="https://fonts.googleapis.com/css2?family=Open+Sans:wght@400;600&display=swap">
<style>
  :root {
    --backdrop: #e6e7e8;
    --card-white: #ffffff;
    --brand-blue: #139fd9;
    --bulb-light: #8fd0ee;
    --ink: #111417;
    --paper-white: #ffffff;
  }
  * { margin: 0; padding: 0; box-sizing: border-box; }
  html, body {
    width: 1200px; height: 1000px; overflow: hidden;
    background: var(--backdrop);
    font-family: "Open Sans", Arial, sans-serif;
  }
  .canvas {
    position: relative; width: 1200px; height: 1000px;
    display: flex; align-items: center; justify-content: center;
  }
  .business-card {
    position: relative; width: 900px; height: 514px;
    background: var(--card-white);
    box-shadow: 0 12px 30px rgba(0,0,0,0.18);
    overflow: hidden;
  }
  .blue-band { position: absolute; inset: 0; }
  .bulb-illustration {
    position: absolute; left: 80px; top: 90px;
    width: 260px; height: 250px; border-radius: 50%;
    background: radial-gradient(circle at 50% 50%, var(--bulb-light) 0%, rgba(143,208,238,0.35) 60%, rgba(143,208,238,0) 72%);
  }
  .brand-name {
    position: absolute; right: 70px; top: 70px;
    font-size: 54px; font-weight: 400; color: var(--brand-blue);
    letter-spacing: 1px;
  }
  .contact-name {
    position: absolute; right: 150px; top: 218px;
    font-size: 27px; font-weight: 400; color: var(--ink);
    text-transform: uppercase; letter-spacing: 0.5px;
  }
  .contact-title {
    position: absolute; right: 150px; top: 256px;
    font-size: 21px; color: var(--paper-white);
  }
  .contact-line {
    position: absolute; display: flex; align-items: center; gap: 10px;
    font-size: 22px; color: var(--paper-white);
  }
  .contact-line svg { width: 22px; height: 22px; flex: none; }
  .contact-email { right: 60px; top: 318px; }
  .contact-phone { left: 120px; top: 392px; font-size: 25px; }
  .tagline {
    position: absolute; left: 120px; top: 440px;
    font-size: 25px; color: var(--ink);
  }
</style>
</head>
<body>
<main class="canvas">
  <section class="business-card">
    <svg class="blue-band" viewBox="0 0 900 514" width="900" height="514" aria-hidden="true">
      <path d="M0 262 H230 V200 H900 V514 H0 Z" fill="var(--brand-blue)"/>
    </svg>

    <div class="bulb-illustration" role="img" aria-label="Brush-drawn light bulb with radiating rays, half blue on white and half white on blue"></div>

    <div class="brand-name">Frame And Form</div>

    <div class="contact-name">Megan T Dulcoff</div>
    <div class="contact-title">Senior Design Specialist</div>

    <div class="contact-line contact-email">
      <svg viewBox="0 0 22 22" aria-hidden="true">
        <circle cx="11" cy="11" r="11" fill="var(--paper-white)"/>
        <circle cx="12.5" cy="9.5" r="3.6" fill="none" stroke="var(--brand-blue)" stroke-width="1.8"/>
        <line x1="9.8" y1="12.2" x2="6.5" y2="15.5" stroke="var(--brand-blue)" stroke-width="2" stroke-linecap="round"/>
      </svg>
      <span>megan@frameandform.example</span>
    </div>

    <div class="contact-line contact-phone">
      <svg viewBox="0 0 22 22" aria-hidden="true">
        <circle cx="11" cy="11" r="11" fill="var(--paper-white)"/>
        <path d="M7.2 5.5c.5-.4 1.2-.3 1.5.2l1.1 1.8c.3.5.2 1.1-.2 1.4l-.7.6c.6 1.4 1.6 2.5 3 3.1l.6-.7c.4-.4 1-.5 1.4-.2l1.8 1.1c.5.3.6 1 .2 1.5l-.8.9c-.6.6-1.5.8-2.3.5-3-1.2-5.3-3.5-6.4-6.4-.3-.8-.1-1.7.5-2.3z" fill="var(--brand-blue)"/>
      </svg>
      <span>240-555-0193</span>
    </div>

    <p class="tagline">Bringing bright Ideas to Interiors, Exteriors &amp; Home Staging</p>
  </section>
</main>
</body>
</html>
```